Brightwell Capital - fund management and algorithmic design

We're looking for a web design for a new company called brightwell capital which is based out of London.

The photography provided will be a major part of the creative content. The intent is to have a sharp, clear, professional, slick look. Less is more and clutter is not the root that should be followed.

A logo has been selected and the photography provided will give the designer a good idea of what we are looking for. The logo designer is still getting back to me with the very final version but what is provided is good enough to move forward with. the final design will likely have this changed slightly.

The photos are about 1.2 meg each at 86 pdi. I believe this is about right for a high quality web image.

At some point on the site it should have: Integrity, Innovative, Progressive. These are core principles of the company. Also ,Fund management and algorithmic design could be used somewhere as this explains exactly what we do.

I also wish to have the secondary pages designed too. However, rather than asking everybody to do this i will ask a select few designers to look at one of the pages. The chosen designer will then be asked to finish the other pages too. These are expected to be quite simple, nothing fussy - clean and presentable with a small amount of room for artistic license.

Also the links to these two sites will give you a very good idea of what we're looking for.

quendor.com
tavelpointrix.com
birchwardlanefx.com
Updates

Hi,

sorry for as i had problem getting the final images from the photographer as he's been away and busy.

However, we now the the logo (be it not the very final version) and the photos uploaded.  Please read the brief again as this has been updated too.

Initially i'd be happy if you made up the front page and after that i will ask a small handful of designers to submit a design for the secondary page - this way i feel is better as it uses less of your time.  These pages are likely to use the photography for a backdrop too.

Looking forward to your designs.

Regards,

Dominic

Reason: I have extended the deadline as the first week has been held up because of delays in content. thanks, Dominic

Target Market(s)

wealth individuals who wish to diversify their investment portfolios with investments predominantly in the foreign exchange markets as well as some financial products offered by ZPLHoldings.com

Industry/Entity Type

It Company

Requirements
Must have
• There are three photos that the site must use, once the final design is fully operational and coded we want the first three photos to rotate on the front page. Much like quendorr.com

An area where a prospective client can enter their email address to receive market new letters and correspondences from brightwell capital.

front page

about us,
managed accounts
systems and performance

```html
<!DOCTYPE html>
<html lang="en">
<head>
<meta charset="utf-8">
<title>Company Name</title>
<link rel="stylesheet" href="https://fonts.googleapis.com/css2?family=Quicksand:wght@400;500&display=swap">
<style>
  :root {
    --page-white: #ffffff;
    --ocean-deep: #081632;
    --ocean-mid: #1a3566;
    --ocean-light: #33578c;
    --fuselage: rgba(222, 228, 238, 0.55);
    --fuselage-soft: rgba(190, 204, 224, 0.32);
    --panel-tint: rgba(8, 14, 30, 0.6);
    --text-light: #ffffff;
    --rule: rgba(255, 255, 255, 0.7);
    --footer-black: #000000;
  }
  * { margin: 0; padding: 0; box-sizing: border-box; }
  html, body {
    width: 1200px; height: 940px; overflow: hidden;
    background: var(--page-white);
    font-family: "Quicksand", sans-serif;
    color: var(--text-light);
  }
  .site { position: relative; width: 1200px; height: 940px; }
  .hero-photo {
    position: absolute; left: 0; top: 31px; width: 1200px; height: 842px;
    background:
      radial-gradient(ellipse 260px 150px at 1010px 610px, var(--fuselage), transparent 72%),
      radial-gradient(ellipse 420px 120px at 760px 470px, var(--fuselage-soft), transparent 72%),
      radial-gradient(ellipse 340px 80px at 200px 560px, var(--fuselage-soft), transparent 72%),
      radial-gradient(ellipse 180px 60px at 1060px 220px, var(--fuselage-soft), transparent 72%),
      radial-gradient(ellipse 200px 60px at 420px 130px, var(--fuselage-soft), transparent 72%),
      linear-gradient(175deg, var(--ocean-light) 0%, var(--ocean-mid) 45%, var(--ocean-deep) 100%);
  }
  .intro-panel {
    position: absolute; left: 281px; top: 94px; width: 647px; height: 730px;
    background: var(--panel-tint);
  }
  .contact-bar {
    position: absolute; top: 123px; left: 307px; right: 290px;
    display: flex; justify-content: space-between; align-items: center;
    font-size: 16px; letter-spacing: 0.5px;
  }
  .contact-item { display: flex; align-items: center; gap: 7px; }
  .brand {
    position: absolute; left: 281px; width: 647px; top: 200px;
    display: flex; flex-direction: column; align-items: center; gap: 14px;
  }
  .brand-dot { width: 30px; height: 30px; border-radius: 50%; background: var(--text-light); }
  .brand-name { font-size: 50px; font-weight: 500; letter-spacing: 0.5px; line-height: 1; }
  .main-nav {
    position: absolute; left: 316px; width: 576px; top: 341px;
    border-top: 1px solid var(--rule);
    padding-top: 11px; height: 40px;
    font-size: 18px; letter-spacing: 0.8px;
  }
  .main-nav a { position: absolute; color: var(--text-light); text-decoration: none; }
  .nav-home { left: 0; }
  .nav-about { left: 122px; }
  .nav-managed { left: 304px; }
  .nav-contact { right: 0; }
  .tagline {
    position: absolute; left: 281px; width: 647px; top: 476px;
    text-align: center; font-size: 25px; font-weight: 400; letter-spacing: 1px;
  }
  .mission {
    position: absolute; left: 325px; width: 560px; top: 539px;
    text-align: center; font-size: 17.5px; line-height: 23px; letter-spacing: 0.6px;
  }
  .slide-dots {
    position: absolute; left: 281px; width: 647px; top: 777px;
    display: flex; justify-content: center; gap: 8px;
  }
  .slide-dots span {
    width: 14px; height: 14px; border-radius: 50%;
    background: var(--text-light); border: 3px solid var(--text-light);
    box-shadow: inset 0 0 0 2px var(--ocean-deep);
  }
  .site-footer {
    position: absolute; left: 0; top: 873px; width: 1200px; height: 67px;
    background: var(--footer-black);
    display: flex; justify-content: center; align-items: center;
    font-size: 14px; font-weight: 500; letter-spacing: 0.3px;
  }
</style>
</head>
<body>
<div class="site">
  <div class="hero-photo" role="img" aria-label="Photograph of a white private jet flying low over a deep blue sea"></div>
  <div class="intro-panel"></div>

  <header class="contact-bar">
    <span class="contact-item">
      <svg width="22" height="14" viewBox="0 0 22 14" aria-hidden="true">
        <rect x="0.5" y="0.5" width="21" height="13" fill="#fff"/>
        <path d="M0.5 0.5 L11 8 L21.5 0.5" fill="none" stroke="#081632" stroke-width="1.4"/>
      </svg>
      contact@halvercove.com
    </span>
    <span class="contact-item">
      <svg width="20" height="16" viewBox="0 0 20 16" aria-hidden="true">
        <path d="M1 5 Q10 -1 19 5 L17 7 L14 5 L14 3 Q10 2 6 3 L6 5 L3 7 Z" fill="#fff"/>
        <path d="M5 7 L15 7 L17 15 L3 15 Z" fill="#fff"/>
        <circle cx="10" cy="11" r="2.2" fill="#081632"/>
      </svg>
      ( 0200 ) 4815 627
    </span>
  </header>

  <div class="brand">
    <span class="brand-dot"></span>
    <span class="brand-name">Company Name</span>
  </div>

  <nav class="main-nav">
    <a class="nav-home" href="#">HOME</a>
    <a class="nav-about" href="#">About us</a>
    <a class="nav-managed" href="#">Managed</a>
    <a class="nav-contact" href="#">Contact</a>
  </nav>

  <h1 class="tagline">Integrity, Innovation and Independence</h1>
  <p class="mission">Our entire organisation is dedicated to offering clients the highest levels of service and discretion and access to commodity and financial markets globally.</p>

  <div class="slide-dots"><span></span><span></span><span></span></div>

  <footer class="site-footer">Company Name Copyright 2013! All rights Reserved!</footer>
</div>
</body>
</html>
```